Funky Bali beach wedding invitation

Wedding invitation for a beach wedding in Bali

The design needs to be colorful and fun and send a message of happiness & love with a beach theme.

The names of the couple getting married are Milo & Rena

Industry/Entity Type

Wedding

```html
<!DOCTYPE html>
<html lang="en">
<head>
<meta charset="utf-8">
<title>Milo &amp; Rena — Beach Wedding Invitation</title>
<link href="https://fonts.googleapis.com/css2?family=Pinyon+Script&family=Libre+Baskerville&family=Josefin+Sans:wght@400&family=Open+Sans:wght@400&display=swap" rel="stylesheet">
<style>
  :root{
    --page:#c9cbcd;
    --board:#062740;
    --ocean:#0a84bf;
    --ocean-deep:#0a6fa6;
    --sand:#e8e9eb;
    --ink:#176b98;
    --ink-dark:#1b1b1b;
    --foam:#9fd0e3;
    --foam-soft:#bfe0ec;
    --coral:#e8641f;
    --sun:#f2b32a;
    --shell:#c9cbce;
    --label:#d7dde3;
    --rule:#3c5568;
  }
  *{margin:0;padding:0;box-sizing:border-box}
  html,body{width:1169px;height:1200px;overflow:hidden;background:var(--page)}
  .canvas{position:relative;width:1169px;height:1200px}
  .board{position:absolute;left:14px;top:15px;width:1141px;height:1121px;background:var(--board);border-radius:52px}
  .abs{position:absolute}
  .card{position:absolute;overflow:hidden;box-shadow:0 14px 24px rgba(0,0,0,.55)}
  .card--outside{left:116px;top:104px;width:950px;height:411px;background:var(--ocean)}
  .card--inside{left:116px;top:630px;width:952px;height:412px;background:var(--ocean);border:2px solid var(--ocean-deep)}
  .band{left:0;top:127px;width:100%;height:167px;background:var(--sand)}
  .fold{top:0;width:1px;height:100%;background:rgba(255,255,255,.12)}
  .script{font-family:"Pinyon Script",cursive}
  .quote{color:var(--foam);font-size:21px;line-height:24px;text-align:center;white-space:nowrap;transform:translateX(-50%)}
  .couple{color:var(--ink);white-space:nowrap;transform:translateX(-50%)}
  .date{font-family:"Josefin Sans",sans-serif;color:var(--ink-dark);white-space:nowrap;transform:translateX(-50%);display:flex;align-items:center;gap:8px}
  .date::before,.date::after{content:"";display:block;width:30px;height:1px;background:var(--ink-dark)}
  .monogram .date::before,.monogram .date::after{width:16px}
  .starfish{border-radius:50%}
  .starfish--shell{background:radial-gradient(ellipse,var(--shell) 40%,rgba(201,203,206,0) 72%)}
  .starfish--sea{background:radial-gradient(ellipse,#3f93bd 40%,rgba(63,147,189,0) 72%)}
  .starfish--warm{background:radial-gradient(ellipse at 40% 45%,var(--coral) 30%,var(--sun) 55%,rgba(242,179,42,0) 74%)}
  .flourish{background:radial-gradient(ellipse,#d6d7d9 30%,rgba(214,215,217,0) 70%)}
  .water{background:linear-gradient(rgba(159,208,227,0),var(--foam) 70%)}
  .water--top{background:linear-gradient(var(--foam-soft),rgba(191,224,236,0))}
  .panel{left:217px;top:18px;width:718px;height:378px;background:var(--sand);overflow:hidden}
  .details{position:absolute;left:737px;top:0;transform:translateX(-50%);text-align:center;font-family:"Libre Baskerville",serif;color:var(--ink);font-size:10.5px;white-space:nowrap}
  .details p{position:absolute;left:50%;transform:translateX(-50%)}
  .monogram{left:34px;top:126px;width:147px;height:119px;background:var(--ocean-deep)}
  .monogram__inner{position:absolute;left:10px;top:10px;right:10px;bottom:10px;background:#fff}
  .label{position:absolute;left:0;width:1169px;text-align:center;font-family:"Open Sans",sans-serif;font-size:21px;color:var(--label)}
  .rule{position:absolute;height:1px;background:var(--rule)}
  .footer{position:absolute;left:14px;top:1136px;width:1141px;height:44px;background:linear-gradient(#e6e7e8,#c9cbcd)}
</style>
</head>
<body>
<main class="canvas">
  <div class="board"></div>

  <section class="card card--outside" aria-label="Invitation outside">
    <div class="abs band"></div>
    <div class="abs water" role="img" aria-label="Soft sea wave illustration" style="left:0;top:256px;width:473px;height:38px"></div>
    <div class="abs fold" style="left:473px"></div>
    <div class="abs starfish starfish--shell" role="img" aria-label="Pair of pale grey starfish illustration" style="left:150px;top:140px;width:210px;height:150px"></div>
    <p class="abs script quote" style="left:236px;top:306px">Only from the heart<br>Can you touch the sky</p>

    <div class="abs starfish starfish--warm" role="img" aria-label="Orange and yellow starfish illustration" style="left:660px;top:138px;width:115px;height:76px"></div>
    <div class="abs flourish" role="img" aria-label="Faint swirl ornament" style="left:608px;top:222px;width:80px;height:36px"></div>
    <div class="abs flourish" role="img" aria-label="Faint swirl ornament" style="left:948px;top:222px;width:80px;height:36px"></div>
    <p class="abs script couple" style="left:717px;top:207px;font-size:36px;line-height:44px">Milo and Rena</p>
    <p class="abs date" style="left:717px;top:258px;font-size:15px"><span>DECEMBER 11, 2011</span></p>
  </section>

  <p class="label" style="top:528px">outside</p>
  <div class="rule" style="left:124px;top:558px;width:420px"></div>
  <div class="rule" style="left:642px;top:558px;width:420px"></div>

  <section class="card card--inside" aria-label="Invitation inside">
    <div class="abs fold" style="left:476px"></div>
    <div class="abs panel">
      <div class="abs water--top" role="img" aria-label="Soft sea wave illustration" style="left:0;top:0;width:718px;height:46px"></div>
      <p class="abs script quote" style="left:125px;top:160px;color:#5aaed3">Only from the heart<br>Can you touch the sky</p>
    </div>
    <div class="abs water" role="img" aria-label="Layered sea wave illustration" style="left:0;top:322px;width:952px;height:90px"></div>

    <div class="abs monogram">
      <div class="monogram__inner">
        <div class="abs starfish starfish--warm" role="img" aria-label="Small orange and yellow starfish illustration" style="left:36px;top:6px;width:54px;height:36px"></div>
        <p class="abs script couple" style="left:63px;top:42px;font-size:17px;line-height:20px">Milo and Rena</p>
        <p class="abs date" style="left:63px;top:74px;font-size:8px"><span>DECEMBER 11, 2011</span></p>
      </div>
    </div>

    <div class="abs starfish starfish--sea" role="img" aria-label="Blue and pale grey starfish illustration" style="left:80px;top:244px;width:215px;height:150px"></div>
    <div class="abs starfish starfish--warm" role="img" aria-label="Orange and yellow starfish illustration" style="left:816px;top:313px;width:125px;height:85px"></div>

    <div class="details">
      <p style="top:72px">MR AND MRS .......................</p>
      <p style="top:94px">REQUEST THE HONOR OF YOUR PRESENCE</p>
      <p style="top:120px">AT THE MARRIAGE OF THEIR SON</p>
      <p class="script" style="top:148px;font-size:32px;line-height:40px">Milo and Rena</p>
      <p style="top:203px">DAUGHTER OF MR AND MRS............................</p>
      <p style="top:231px">SATURDAY THE ... OF DECEMBER</p>
      <p style="top:253px">TWO THOUSAND ELEVEN</p>
      <p style="top:273px">AT................................................</p>
      <p style="top:295px">FIVE O’CLOCK IN THE EVENING</p>
    </div>
  </section>

  <p class="label" style="top:1054px">inside</p>
  <div class="rule" style="left:114px;top:1084px;width:420px"></div>
  <div class="rule" style="left:632px;top:1084px;width:420px"></div>

  <div class="footer"></div>
</main>
</body>
</html>
```